Medical Internet Marketing Company Needs a Site!

We need a new, fresh website for our search engine optimization and social media marketing company. We specialize in helping medical practices, doctors, physicians, and hospitals with their online presence and web ranking. The site should lean towards being suited for these audiences.

We have several examples of website that we like as well as things that we like about them.

Here are sites that we enjoy.

www.brightwavelab.com

It's a good design for the site all around. The videos, buttons, and images are all excellent. They did a fine job.

- We really like their "contact us" side bar and want to include one like it on the secondary pages.

www.corvantis.net

- We don't like the "thickness" of the top navigation bar.
- We like the page colors, easy navigation, and big call to action phone number in the top right corner.

http://www.teluvo.com/

Out of all the examples provided, Teluvo is our favorite and closest look and style to what we are looking for.

- We really like the openness of the design, such as space between the text and background.

- We want a price page in a style very similar to their pricing page with the services listed and check-marks, etc. although we intend to have multiple service package columns much like Corvantis's SEO pricing page.

- The way the video fits into the home page header is very organized, simple, and attention grabbing. We intend to place a slider with videos here.

- We need a page design that will allow for an image slider like Teluvo's Features page.

Here's a great example of a medical internet marketing website: http://www.dermaplex.com/

Target Market(s)

Our target market is doctors, typically male and typically 40-45 years old. I

Industry/Entity Type

Marketing

Requirements
Must have
• The homepage should have a slider in the video. Interior pages should have a video in the very top similar to how they do it on www.brightwavelab.com

The top navigation tabs needed are:
- Home
- Solutions
- Resources
- About
- Why Quelvo
- Contact

The sidebar should have a GREAT call to action in it on interior pages.

There should be one interior page that is similar to this - http://www.teluvo.com/pricing/

There needs to be a page with multiple boxes that take up a row of the web page's body. This page will house all the case studies similar to brightwave lab's: http://www.brightwavelab.com/success-stories/case-studies/ The one exception is we want the case studies to be inside of "boxes" instead of between horizontal lines like brightwave lab's.
Nice to have
• Color, professional, and clean. GREAT use of calls to actions.

```html
<!DOCTYPE html>
<html lang="en">
<head>
<meta charset="utf-8">
<title>Quelvo — Medical Internet Marketing</title>
<link href="https://fonts.googleapis.com/css2?family=Open+Sans:wght@400;600;700&display=swap" rel="stylesheet">
<style>
:root{
  --bg-top:#2e4759;
  --bg-mid:#1d3142;
  --bg-bottom:#0d1822;
  --navy:#0c2238;
  --navy-text:#102a44;
  --panel-dark:#0f2235;
  --panel-dark-2:#1b3247;
  --hero-light:#7391a6;
  --hero-dark:#3a586e;
  --line:#cfd8de;
  --text-light:#e4e9ed;
  --text-soft:#c4ccd3;
  --white:#ffffff;
  --tile-light:#ffffff;
  --tile-dark:#d5d8db;
}
*{margin:0;padding:0;box-sizing:border-box}
html,body{width:1117px;height:1200px;overflow:hidden;background:var(--bg-bottom)}
body{position:relative;font-family:"Open Sans",sans-serif;color:var(--text-light)}
.page{
  position:absolute;left:0;top:0;width:1024px;height:1100px;overflow:hidden;
  transform:scale(1.0908);transform-origin:0 0;
  background:radial-gradient(ellipse at 50% 20%,var(--bg-top) 0%,var(--bg-mid) 55%,var(--bg-bottom) 100%);
}
.abs{position:absolute}
.brand{left:55px;top:58px;display:flex;align-items:center;gap:14px}
.brand-square{width:70px;height:46px;background:var(--text-soft)}
.brand-name{font-size:52px;font-weight:400;letter-spacing:4px;color:var(--text-soft);line-height:1}
.phone-box{left:724px;top:15px;width:284px;height:57px;border:1px solid var(--text-soft);display:flex;align-items:center;justify-content:center;gap:6px}
.phone-number{font-size:34px;color:var(--white);letter-spacing:.5px}
.main-nav{left:484px;top:148px;display:flex;gap:18px;font-size:16px;color:var(--text-soft)}
.main-nav .current{color:var(--white)}
.hero-panel{left:0;top:162px;width:445px;height:310px;border:1px solid var(--line);border-left:none;
  background:radial-gradient(ellipse at 45% 35%,var(--hero-light),var(--hero-dark));text-align:center}
.hero-mark{position:absolute;left:170px;top:36px;width:70px;height:38px;background:var(--navy)}
.hero-title{position:absolute;left:0;width:445px;top:88px;font-size:21px;line-height:28px;color:var(--navy-text);font-weight:400}
.hero-text{position:absolute;left:40px;width:365px;top:150px;font-size:15px;line-height:19px;color:var(--white)}
.cta-bracket{position:absolute;left:12px;top:245px;width:20px;height:62px;border:3px solid var(--navy);border-right:none}
.cta-button{position:absolute;left:20px;top:252px;width:325px;height:44px;background:var(--navy);
  clip-path:polygon(0 0,100% 0,88% 100%,0 100%);color:var(--white);font-size:19px;line-height:44px;text-align:left;padding-left:39px}
.slider-dots{position:absolute;left:356px;top:286px;display:flex;gap:6px}
.slider-dots span{width:14px;height:14px;background:var(--navy)}
.slider-dots .active{background:var(--white)}
.video-frame{left:460px;top:174px;width:525px;height:287px;background:var(--white);box-shadow:0 2px 10px #0008}
.video-still{position:absolute;left:16px;top:16px;width:493px;height:256px;background:linear-gradient(90deg,#eceeef 0%,#cfd3d6 50%,#b6bbbf 100%)}
.video-label{position:absolute;right:14px;top:6px;text-align:right;color:var(--navy-text)}
.video-label strong{display:block;font-size:16px;font-weight:400}
.video-label small{display:block;font-size:10px;line-height:10px}
.play-button{position:absolute;left:21px;top:145px}
.edge-panel{left:997px;top:162px;width:27px;height:310px;border:1px solid var(--line);border-right:none}
.specialty-row{left:55px;top:485px;display:flex;gap:7px}
.specialty-tile{width:222px;height:120px;border:2px solid #8c8f92;background:linear-gradient(90deg,var(--tile-light) 40%,var(--tile-dark));display:flex;align-items:center;padding-left:24px;font-size:16px;line-height:19px;color:var(--navy-text)}
.row-arrow{top:534px;font-size:30px;color:var(--text-soft);line-height:1}
.info-panel{top:623px;width:472px;height:282px;background:linear-gradient(180deg,var(--panel-dark),var(--panel-dark-2));box-shadow:0 2px 8px #0007}
.panel-title{position:absolute;left:0;width:100%;top:36px;text-align:center;font-size:25px;font-weight:400;color:var(--white)}
.testimonial-photo{position:absolute;left:15px;top:79px;width:106px;height:158px;background:linear-gradient(180deg,#bfc3c6,#6d7378)}
.testimonial-quote{position:absolute;left:135px;top:77px;width:318px;font-size:12.5px;line-height:16.2px;font-weight:600;text-align:justify;color:var(--white)}
.testimonial-author{position:absolute;left:135px;top:253px;font-size:13px;font-weight:600;color:var(--white)}
.panel-sub{position:absolute;left:0;width:100%;top:76px;text-align:center;font-size:14px;line-height:18px;color:var(--white)}
.client{position:absolute;font-size:21px;font-weight:600;color:var(--white)}
.more-link{top:911px;font-size:13px;font-weight:600;color:var(--text-soft);letter-spacing:.3px}
.footer-brand{left:51px;top:972px;display:flex;align-items:center;gap:12px}
.footer-brand .brand-square{width:60px;height:34px}
.footer-brand .brand-name{font-size:38px;letter-spacing:3px}
.footer-nav{left:51px;top:1015px;font-size:15px;color:var(--text-light);word-spacing:2px}
.copyright{left:51px;top:1038px;font-size:12px;color:var(--text-light)}
.social-title{left:812px;top:974px;font-size:15px;font-weight:700;color:var(--white)}
.social-row{left:692px;top:995px;display:flex;gap:6px}
.social-row span{width:42px;height:44px;border:2px solid #d8dde0;border-radius:4px 4px 21px 21px}
.footer-band{left:0;top:1075px;width:1024px;height:25px;background:#0a131b;border-top:1px solid #22384a}
</style>
</head>
<body>
<div class="page">
  <header>
    <div class="abs brand"><span class="brand-square"></span><span class="brand-name">QUELVO</span></div>
    <div class="abs phone-box">
      <svg width="30" height="38" viewBox="0 0 30 38" aria-hidden="true"><path d="M8 2 L13 9 L10 13 Q12 22 18 27 L22 24 L28 30 L24 36 Q10 34 4 14 Q3 6 8 2Z" fill="#fff"/></svg>
      <span class="phone-number">123-456-7890</span>
    </div>
    <nav class="abs main-nav">
      <span class="current">Home</span><span>Solutions</span><span>Resources</span><span>About</span><span>Why Quelvo</span><span>Contact</span>
    </nav>
  </header>

  <section class="abs hero-panel">
    <span class="hero-mark"></span>
    <h1 class="hero-title">MEDICAL INTERNET MARKETING<br>THAT GET RESULTS</h1>
    <p class="hero-text">We specialize in helping medical practices, doctors, physicians, and hospitals with their online presence and web ranking</p>
    <span class="cta-bracket"></span>
    <a class="cta-button">Select Your Speciality !</a>
    <div class="slider-dots"><span></span><span></span><span class="active"></span><span></span></div>
  </section>

  <section class="abs video-frame">
    <div class="video-still" role="img" aria-label="Businessman in a suit flipping through an open book">
      <div class="video-label"><strong>HOW IT WORKS</strong><small>90 Sec Tutorial</small></div>
      <svg class="play-button" width="74" height="74" viewBox="0 0 74 74" aria-label="Play video"><circle cx="37" cy="37" r="34" fill="none" stroke="#0f2a44" stroke-width="3"/><path d="M28 22 L54 37 L28 52Z" fill="#0f2a44"/></svg>
    </div>
  </section>
  <div class="abs edge-panel"></div>

  <span class="abs row-arrow" style="left:22px">«</span>
  <div class="abs specialty-row">
    <div class="specialty-tile" role="img" aria-label="Doctor's coat and stethoscope">MEDICAL<br>PRACTICE</div>
    <div class="specialty-tile" role="img" aria-label="Doctor reading at a desk">DOCTORS</div>
    <div class="specialty-tile" role="img" aria-label="Hand holding a stethoscope">PHYSCIANS</div>
    <div class="specialty-tile" role="img" aria-label="Hospital bed and equipment">HOSPITALS</div>
  </div>
  <span class="abs row-arrow" style="left:972px">»</span>

  <section class="abs info-panel" style="left:30px">
    <h2 class="panel-title">SUCCESS STORIES...</h2>
    <div class="testimonial-photo" role="img" aria-label="Marketing executive seated at his desk"></div>
    <p class="testimonial-quote">We are very satisfied with the efforts of QUELVO to connect ARVEN USA with our valued consumers via our internet marketing initiatives. Their program is affordable and the relationship from the start has been very thorough and easy to implement. Their ongoing support with their creative and responsive staff has been excellent. We have recommended QUELVO with many of our business associates and will continue to do so.</p>
    <p class="testimonial-author">Harold M., VP Marketing, ARVEN Appliances</p>
  </section>
  <a class="abs more-link" style="left:354px">READ MORE STORIES !</a>

  <section class="abs info-panel" style="left:520px">
    <h2 class="panel-title">OUR CLIENT`S</h2>
    <p class="panel-sub">Some of our clients<br>whom we are working with..</p>
    <div class="client" style="left:48px;top:137px">MedNova</div>
    <div class="client" style="left:276px;top:137px">Verlana</div>
    <div class="client" style="left:48px;top:190px">adsummit</div>
    <div class="client" style="left:268px;top:190px">Triumph Power</div>
  </section>
  <a class="abs more-link" style="left:918px">SEE MORE !</a>

  <footer>
    <div class="abs footer-brand"><span class="brand-square"></span><span class="brand-name">QUELVO</span></div>
    <nav class="abs footer-nav">Home | Solutions | Resources | About | Why Quelvo | Contact</nav>
    <p class="abs copyright">Copyright © 2012 QUELVO. All rights reserved.</p>
    <p class="abs social-title">Get Social With Us !</p>
    <div class="abs social-row">
      <span style="background:#3b5c9a"></span><span style="background:#39a9d9"></span><span style="background:#b8bcbf"></span><span style="background:#4f8f3a"></span><span style="background:#c8ccd0"></span><span style="background:#e89a22"></span>
    </div>
    <div class="abs footer-band"></div>
  </footer>
</div>
</body>
</html>
```